Willowmere Counseling (Endure - Mend - Flourish) - Double Sided Business Card

I would like a 2-sided business card. Front: Matte Black or Navy with Logo & Tagline. Back: Name, Address, Phone Number, Email, & Website (maybe would like to include a small map pin-pointing location); Prefer front to be a gold/silver foil (iridescent); Back prefer white or light colored background with lettering that is easy to read and simple

Target Market(s)

Individuals & Couples (13 y.o. - ALL Adults); High end clientele

Industry/Entity Type

Licensed Professional Counselor (Mental Health)

Contact Information for Business Card

Name: Willowmere Counseling; Tagline: Endure - Mend - Flourish; Address: 3870 N. Garrick Ave., Suite 214, Fort Worth, TX 76132; Phone: (214) 555-0187; Website: www.WillowmereCounseling.example

Font styles to use
Serif

Requirements
Must have
• Logo on Front (Large) prefer gold/silver foil on a matte dark color (i.e. black, navy, etc.); Back of Card: All other relevant information

```html
<!DOCTYPE html>
<html lang="en">
<head>
<meta charset="utf-8">
<title>Willowmere Counseling – Business Card</title>
<link rel="stylesheet" href="https://fonts.googleapis.com/css2?family=Cinzel:wght@400;600&family=Arimo:wght@400&display=swap">
<style>
  :root {
    --backdrop: #1c1c1d;
    --card: #0b0b0b;
    --gold: #d9b44a;
    --silver: #c9c9cc;
    --grey: #8e8e92;
    --ink-light: #ecebe8;
    --divider: #2a2a2a;
  }
  * { margin: 0; padding: 0; box-sizing: border-box; }
  html, body { width: 1200px; height: 900px; overflow: hidden; }
  body {
    background: radial-gradient(ellipse at 50% 45%, #2a2a2b 0%, var(--backdrop) 70%);
    display: flex; align-items: center; justify-content: center; gap: 40px;
    font-family: "Arimo", Arial, sans-serif;
  }
  .card {
    width: 540px; height: 309px;
    background: var(--card);
    border-radius: 18px;
    box-shadow: 0 18px 40px rgba(0,0,0,.55);
    position: relative;
    overflow: hidden;
  }
  /* Contact side */
  .card--contact { display: flex; }
  .brand-panel {
    width: 52%;
    display: flex; flex-direction: column; align-items: center; justify-content: center;
    padding: 0 18px;
    border-right: 1px solid var(--divider);
  }
  .brand-mark { width: 34px; height: 34px; border-radius: 50%; background: var(--gold); margin-bottom: 14px; }
  .brand-name {
    font-family: "Cinzel", serif; font-weight: 400;
    font-size: 24px; line-height: 1.15; letter-spacing: 1.5px;
    text-align: center; color: var(--gold);
  }
  .brand-rule { width: 80%; height: 2px; background: var(--grey); margin: 10px 0 8px; }
  .brand-tagline {
    font-family: "Cinzel", serif; font-size: 12px; letter-spacing: 1px; color: var(--gold);
  }
  .details-panel {
    width: 48%;
    padding: 52px 22px 0 26px;
    color: var(--ink-light);
  }
  .person-name {
    font-family: "Cinzel", serif; font-weight: 400;
    font-size: 22px; color: var(--gold); letter-spacing: .5px;
  }
  .person-title { font-size: 13px; margin: 2px 0 18px; }
  .contact-list { list-style: none; font-size: 11.5px; line-height: 1.75; }
  .contact-list li { display: flex; align-items: center; gap: 7px; white-space: nowrap; }
  .contact-list svg { width: 12px; height: 12px; flex: none; }
  .site-name { color: var(--gold); }
  .address { font-size: 12.5px; line-height: 1.4; margin-top: 16px; }
  /* Logo side */
  .card--logo {
    display: flex; flex-direction: column; align-items: center; justify-content: center;
  }
  .card--logo .brand-mark {
    background: linear-gradient(135deg, #f2f2f2, #8a8a8e);
    width: 40px; height: 40px;
  }
  .card--logo .brand-name { color: var(--silver); font-size: 30px; }
  .card--logo .brand-rule { width: 62%; background: var(--silver); }
  .card--logo .brand-tagline { color: var(--silver); font-size: 13px; }
</style>
</head>
<body>
  <section class="card card--contact">
    <div class="brand-panel">
      <div class="brand-mark"></div>
      <h1 class="brand-name">Willowmere<br>Counseling</h1>
      <div class="brand-rule"></div>
      <p class="brand-tagline">Endure - Mend - Flourish</p>
    </div>
    <div class="details-panel">
      <h2 class="person-name">DANIEL HARTWELL</h2>
      <p class="person-title">Managing Director</p>
      <ul class="contact-list">
        <li>
          <svg viewBox="0 0 24 24" fill="var(--gold)"><path d="M6.6 10.8a15.1 15.1 0 0 0 6.6 6.6l2.2-2.2c.3-.3.7-.4 1-.2 1.1.4 2.3.6 3.6.6.6 0 1 .4 1 1V20c0 .6-.4 1-1 1A17 17 0 0 1 3 4c0-.6.4-1 1-1h3.5c.6 0 1 .4 1 1 0 1.3.2 2.5.6 3.6.1.3 0 .7-.2 1z"/></svg>
          (214) 555-0187
        </li>
        <li>
          <svg viewBox="0 0 24 24" fill="var(--gold)"><path d="M2 5h20v14H2z" opacity=".9"/><path d="M2 5l10 8 10-8" fill="none" stroke="#0b0b0b" stroke-width="2"/></svg>
          info@WillowmereCounseling.example
        </li>
        <li>
          <svg viewBox="0 0 24 24" fill="none" stroke="var(--gold)" stroke-width="2"><circle cx="12" cy="12" r="10"/><path d="M2 12h20M12 2c3 3 3 17 0 20M12 2c-3 3-3 17 0 20"/></svg>
          <span>www.<span class="site-name">WillowmereCounseling</span>.example</span>
        </li>
      </ul>
      <p class="address">3870 N. Garrick Ave., Suite 214<br>Fort Worth, TX 76132</p>
    </div>
  </section>

  <section class="card card--logo">
    <div class="brand-mark"></div>
    <h1 class="brand-name">Willowmere<br>Counseling</h1>
    <div class="brand-rule"></div>
    <p class="brand-tagline">Endure - Mend - Flourish</p>
  </section>
</body>
</html>
```